Birthday Party Event at Facility

Palmetto Turf House is a soccer facility just outside Miami.
We host birthday parties and send emails 2 months and 1 month away from the start of the child's birthday party.
We need to improve our email marketing campaigns.
Here are our inventory of images: https://files.zenbrookshare.net/share/folders/7QxRt2pLmN8vKd3WsYb6HjF4cA9eUoZ1T?usp=sharing
Here is our current birthday website (you can also download the images from the website):
https://palmettoturfhouse.net/coral-bay-turf-arena-kids-celebration-page.php

```html
<!DOCTYPE html>
<html lang="en">
<head>
<meta charset="utf-8">
<title>Birthday Parties at Palmetto Turf House</title>
<link href="https://fonts.googleapis.com/css2?family=Montserrat:wght@500;600;700;800&family=Questrial&display=swap" rel="stylesheet">
<style>
:root{
  --navy:#12296a;
  --red:#f01a1a;
  --white:#ffffff;
  --ink:#1b1b1b;
  --muted:#6b6b6b;
  --line:#d9dde6;
  --photo-a:#2c3f5c;
  --photo-b:#7a6a52;
  --photo-c:#1e2a40;
}
*{margin:0;padding:0;box-sizing:border-box}
html,body{width:1200px;height:3521px;overflow:hidden;background:var(--white)}
body{position:relative;font-family:"Montserrat",sans-serif;color:var(--ink)}
.abs{position:absolute}

.hero-photo{left:74px;top:0;width:1057px;height:956px;
  background:radial-gradient(ellipse at 50% 35%,var(--photo-b) 0%,var(--photo-a) 55%,var(--photo-c) 100%)}
.brand{left:74px;width:1057px;top:96px;text-align:center;display:flex;justify-content:center;align-items:center;gap:14px}
.brand-dot{width:22px;height:22px;border-radius:50%;background:var(--white)}
.brand-name{font-weight:800;font-size:34px;color:var(--white);letter-spacing:1px}

.intro-band{left:74px;top:956px;width:1057px;height:764px;background:var(--navy)}
.intro-card{left:137px;top:852px;width:934px;height:857px;background:var(--white);text-align:center}
.intro-card .kicker{position:absolute;left:0;right:0;top:52px;font-weight:700;font-size:34px;color:var(--navy)}
.intro-card .headline{position:absolute;left:0;right:0;top:100px;font-weight:800;font-size:66px;color:var(--red);letter-spacing:2px}
.intro-card .sub{position:absolute;left:0;right:0;top:180px;font-weight:700;font-size:33px;color:var(--navy)}
.intro-card .title{position:absolute;left:0;right:0;top:262px;font-weight:800;font-size:58px;color:var(--red);letter-spacing:1px}
.intro-card .venue{position:absolute;left:0;right:0;top:338px;font-weight:800;font-size:44px;color:var(--navy);letter-spacing:1px}
.intro-card .venue small{font-size:34px}
.intro-card .copy{position:absolute;left:57px;right:55px;top:440px;font-family:"Questrial",sans-serif;font-size:21.5px;line-height:28.5px;color:var(--ink);text-align:justify;text-align-last:center}
.btn{position:absolute;left:228px;top:732px;width:466px;height:68px;background:var(--red);border-radius:6px;color:var(--white);font-weight:700;font-size:24px;line-height:68px;text-decoration:none}

.packages-band{left:74px;top:1720px;width:1057px;height:591px;background:var(--navy)}
.packages-title{left:74px;width:1057px;top:1770px;text-align:center;font-weight:500;font-size:35px;color:var(--white)}
.pkg{top:1868px;width:456px;height:292px;background:var(--white);border-radius:7px;overflow:hidden;border:2px solid var(--line)}
.pkg-head{background:var(--red);height:82px;color:var(--white);text-align:center;padding-top:12px}
.pkg-head h3{font-size:24px;font-weight:700}
.pkg-head p{font-size:20px;font-weight:500;margin-top:2px}
.pkg ul{list-style:none;padding:20px 0 0 18px}
.pkg li{display:flex;align-items:center;gap:14px;font-size:15px;font-weight:600;height:32px}
.pkg li svg{flex:none}

.options{left:137px;top:2196px;width:934px;height:157px;background:var(--white);border-radius:7px;border:2px solid var(--line);overflow:hidden}
.options-tab{position:absolute;left:0;top:0;width:52px;height:100%;background:var(--red)}
.options-tab span{position:absolute;left:50%;top:50%;transform:translate(-50%,-50%) rotate(90deg);color:var(--white);font-weight:800;font-size:21px;letter-spacing:2px}
.opt{position:absolute;font-size:13.5px;font-weight:700;line-height:17px}
.opt .price{position:absolute;left:0;color:var(--red);white-space:nowrap}
.opt .price::before{content:"";display:inline-block;border-left:6px solid var(--red);border-top:5px solid transparent;border-bottom:5px solid transparent;margin-right:7px}
.opt .desc{position:absolute;left:74px;white-space:nowrap}
.opt .or{color:var(--muted);font-weight:500}
.opt .extra{color:var(--red)}

.perfect-title{left:0;width:1200px;top:2423px;text-align:center;font-weight:600;font-size:35px;color:var(--red)}
.amenity{top:2537px;width:220px;text-align:center}
.amenity svg{display:block;margin:0 auto}
.amenity p{margin-top:22px;font-size:16px;font-weight:700}

.footer{left:74px;top:2780px;width:1057px;height:665px;background:var(--navy);color:var(--white);text-align:center}
.footer .stat{position:absolute;left:0;right:0;top:86px;font-weight:700;font-size:31px;line-height:37px}
.footer .connect{position:absolute;left:0;right:0;top:230px;font-weight:600;font-size:25px}
.footer .social{position:absolute;left:0;right:0;top:333px;display:flex;justify-content:center;gap:44px;font-weight:600;font-size:20px}
.footer .social span{border:2px solid var(--white);border-radius:8px;padding:8px 14px}
.footer .legal{position:absolute;left:0;right:0;top:452px;font-weight:500;font-size:21px;line-height:36px}
.footer .unsub{position:absolute;left:0;right:0;top:560px;font-weight:500;font-size:21px;color:var(--white);text-decoration:none}
.footer-strip{left:74px;top:3445px;width:1057px;height:76px;background:var(--red)}
</style>
</head>
<body>

<div class="abs hero-photo" role="img" aria-label="Photo of four smiling boys in football jerseys at the indoor arena"></div>
<div class="abs brand"><span class="brand-dot"></span><span class="brand-name">Palmetto Turf House</span></div>

<div class="abs intro-band"></div>
<section class="abs intro-card">
  <p class="kicker">are you looking for</p>
  <h1 class="headline">THE PERFECT</h1>
  <p class="sub">birthday party venue?</p>
  <h2 class="title">BIRTHDAY PARTIES</h2>
  <p class="venue"><small>at</small> PALMETTO TURF HOUSE</p>
  <p class="copy">Palmetto Turf House is Florida’s Largest indoor soccer facility. We feature 3 indoor sport fields, a full service bar, a large birthday party room, on site food and beverage facilities and washrooms/changerooms. Let us work with you to customize a birthday party package that works for you. Have a young child? Consider our bouncy castle. Have an older child that likes soccer but wants some variety with dodgeball or bubble soccer? We have you covered. We provide coaches that have been working with us on our youth programs ensuring you will have a full service experience.</p>
  <a class="btn" href="https://palmettoturfhouse.net/coral-bay-turf-arena-kids-celebration-page.php">Read More</a>
</section>

<div class="abs packages-band"></div>
<h2 class="abs packages-title">Our Birthday Party Packages</h2>

<div class="abs pkg" style="left:137px">
  <div class="pkg-head"><h3>Pro Division Package</h3><p>$495 (+10% staff gratuity)</p></div>
  <ul>
    <li><svg width="18" height="18" viewBox="0 0 18 18"><circle cx="9" cy="9" r="9" fill="#f01a1a"/><path d="M5 9.3l2.6 2.6L13 6.5" stroke="#fff" stroke-width="2.2" fill="none"/></svg>Up to 12 children ($75 additional for up to 20)</li>
    <li><svg width="18" height="18" viewBox="0 0 18 18"><circle cx="9" cy="9" r="9" fill="#f01a1a"/><path d="M5 9.3l2.6 2.6L13 6.5" stroke="#fff" stroke-width="2.2" fill="none"/></svg>2 hours - Soccer Field &amp; Party Room</li>
    <li><svg width="18" height="18" viewBox="0 0 18 18"><circle cx="9" cy="9" r="9" fill="#f01a1a"/><path d="M5 9.3l2.6 2.6L13 6.5" stroke="#fff" stroke-width="2.2" fill="none"/></svg>Coach</li>
    <li><svg width="18" height="18" viewBox="0 0 18 18"><circle cx="9" cy="9" r="9" fill="#f01a1a"/><path d="M5 9.3l2.6 2.6L13 6.5" stroke="#fff" stroke-width="2.2" fill="none"/></svg>Staffed Bar</li>
    <li><svg width="18" height="18" viewBox="0 0 18 18"><circle cx="9" cy="9" r="9" fill="#f01a1a"/><path d="M5 9.3l2.6 2.6L13 6.5" stroke="#fff" stroke-width="2.2" fill="none"/></svg>Bring your own cake/cupcakes</li>
  </ul>
</div>

<div class="abs pkg" style="left:615px">
  <div class="pkg-head"><h3>Grand Finals Package</h3><p>$695 (+10% staff gratuity)</p></div>
  <ul>
    <li><svg width="18" height="18" viewBox="0 0 18 18"><circle cx="9" cy="9" r="9" fill="#f01a1a"/><path d="M5 9.3l2.6 2.6L13 6.5" stroke="#fff" stroke-width="2.2" fill="none"/></svg>Up to 20 children</li>
    <li><svg width="18" height="18" viewBox="0 0 18 18"><circle cx="9" cy="9" r="9" fill="#f01a1a"/><path d="M5 9.3l2.6 2.6L13 6.5" stroke="#fff" stroke-width="2.2" fill="none"/></svg>3 hours - Soccer Field &amp; Party Room</li>
    <li><svg width="18" height="18" viewBox="0 0 18 18"><circle cx="9" cy="9" r="9" fill="#f01a1a"/><path d="M5 9.3l2.6 2.6L13 6.5" stroke="#fff" stroke-width="2.2" fill="none"/></svg>Coach</li>
    <li><svg width="18" height="18" viewBox="0 0 18 18"><circle cx="9" cy="9" r="9" fill="#f01a1a"/><path d="M5 9.3l2.6 2.6L13 6.5" stroke="#fff" stroke-width="2.2" fill="none"/></svg>Staffed Bar</li>
    <li><svg width="18" height="18" viewBox="0 0 18 18"><circle cx="9" cy="9" r="9" fill="#f01a1a"/><path d="M5 9.3l2.6 2.6L13 6.5" stroke="#fff" stroke-width="2.2" fill="none"/></svg>Bring your own cake/cupcakes</li>
  </ul>
</div>

<div class="abs options">
  <div class="options-tab"><span>OPTIONS</span></div>
  <div class="opt" style="left:67px;top:13px;width:400px">
    <span class="price" style="top:0">$100</span><span class="desc" style="top:0">Bring your own food / non-alcoholic drinks</span>
    <span class="desc or" style="top:20px">or</span>
    <span class="price" style="top:45px">$150</span><span class="desc" style="top:45px">Pizza Party (3 large pizzas, cooler of<br>sodas/waters)</span>
    <span class="desc extra" style="top:81px">▸ $30 -extra pizzas</span>
  </div>
  <div class="opt" style="left:506px;top:13px;width:400px">
    <span class="price" style="top:0">$150</span><span class="desc" style="top:0">Each extra hour for field/room</span>
    <span class="price" style="top:29px">$100</span><span class="desc" style="top:29px">25 drink bar package (alcoholic drinks)</span>
    <span class="desc extra" style="top:50px">▸ $5 -each additional drink</span>
    <span class="price" style="top:81px">$100</span><span class="desc" style="top:81px">Bouncy castle</span>
    <span class="price" style="top:110px">$50</span><span class="desc" style="top:110px">Video games on the big screen</span>
  </div>
</div>

<h2 class="abs perfect-title">The Perfect Place for a Birthday Party</h2>

<div class="abs amenity" style="left:101px">
  <svg width="90" height="86" viewBox="0 0 90 86" fill="none" stroke="#1b1b1b" stroke-width="3">
    <rect x="6" y="6" width="34" height="26"/><path d="M12 26l9-10 7 7 5-5 5 8"/>
    <path d="M62 10h14l4 12H58z"/><path d="M69 22v14"/>
    <path d="M14 50h62v18H14z"/><path d="M8 44h10v28H8zM72 44h10v28H72z"/>
    <path d="M8 72v8M82 72v8"/><path d="M28 58l4 4M32 58l-4 4M43 58l4 4M47 58l-4 4M58 58l4 4M62 58l-4 4"/>
  </svg>
  <p>Comfortable Venue</p>
</div>
<div class="abs amenity" style="left:346px">
  <svg width="90" height="86" viewBox="0 0 90 86" fill="none" stroke="#1b1b1b" stroke-width="3">
    <rect x="6" y="10" width="78" height="30" rx="6"/><path d="M18 30h54"/>
    <path d="M30 50c-4 5 4 9 0 15M45 50c-4 5 4 9 0 15M60 50c-4 5 4 9 0 15"/>
  </svg>
  <p>Air Conditioned Facility</p>
</div>
<div class="abs amenity" style="left:588px">
  <svg width="90" height="86" viewBox="0 0 90 86" fill="none" stroke="#1b1b1b" stroke-width="4" stroke-linecap="round">
    <path d="M14 24a44 44 0 0 1 62 0"/><path d="M24 34a30 30 0 0 1 42 0"/><path d="M34 44a16 16 0 0 1 22 0"/>
    <circle cx="45" cy="54" r="3" fill="#1b1b1b"/>
    <text x="45" y="84" text-anchor="middle" font-family="Montserrat,sans-serif" font-weight="800" font-size="20" fill="#1b1b1b" stroke="none" letter-spacing="3">FREE</text>
  </svg>
  <p>Free Wifi</p>
</div>
<div class="abs amenity" style="left:841px">
  <svg width="90" height="86" viewBox="0 0 90 86" fill="none" stroke="#1b1b1b" stroke-width="3">
    <path d="M45 4v78M8 43h74"/>
    <rect x="10" y="8" width="14" height="30" rx="2"/><rect x="66" y="48" width="14" height="30" rx="2"/>
    <text x="38" y="34" text-anchor="middle" font-family="Montserrat,sans-serif" font-weight="600" font-size="24" fill="#1b1b1b" stroke="none">P</text>
    <text x="58" y="34" text-anchor="middle" font-family="Montserrat,sans-serif" font-weight="600" font-size="24" fill="#1b1b1b" stroke="none">P</text>
    <rect x="66" y="8" width="14" height="30" rx="2"/>
    <text x="22" y="74" text-anchor="middle" font-family="Montserrat,sans-serif" font-weight="600" font-size="24" fill="#1b1b1b" stroke="none">P</text>
    <rect x="50" y="48" width="12" height="30" rx="2"/>
  </svg>
  <p>Plenty of Parking</p>
</div>

<footer class="abs footer">
  <p class="stat">More than 88.000 Kids are Happy<br>Celebrating their birthday party with us</p>
  <p class="connect">Connect with Us</p>
  <div class="social"><span>Photos</span><span>Page</span><span>News</span></div>
  <p class="legal">2023 Palmetto Turf House. All Rights Reserved.<br>1270 NW Coral Way, Coral Bay, FL 33190</p>
  <a class="unsub" href="#">unsubscribe from this list</a>
</footer>
<div class="abs footer-strip"></div>

</body>
</html>
```